New look and feel for investment website

Hi

Our website needs a crisp and professional look and feel applying to it. Here’s the address: http://www.brightplinth.co.uk. Since posting the brief yesterday (Tuesday, 16 August), we've reduced the amount of content on the home page, which should make life a little easier for you. We will come back later today, with some points of reference in terms of sites we like the look of. (See below)

17 August, 1.20pm GMT. OK, comments generally on the designs submitted so far. Please keep in mind that images of graphs, piles of coins, paper money and pretty females are not what is required. Better to think in terms of abstract imagery instead. Ratios? Circles? Relationships? Patterns? Not money,sex,graphs etc. Hope that helps.

For guidance on look and feel, please refer to these sites, which we like:

http://www.morvelle.co.uk/
http://www.qz.com/
https://www.harrowfieldtamsin.com
https://www.pirelconcerns.com
https://www.kvantule.com
Updates

Here's the Tall Beacons logo created in AI CS5.

Our market is professional financial advisers and relatively sophisticated private investors. The look and feel therefore should be slick and sophisticated - not 'lively' and lightweight, more like a banking site. Please read the brief again where we've added a list of websites that we really like the look of to get a better feel for what we're looking for. Thanks once again, we appreciate the work you're putting in.

It's essential that all the elements that are on the current home page be included on all new designs. 

We use a device in our e-mails which you may wish to incorporate in your design.

Target Market(s)

Professional financial advisers. People who know about investment and money.

Industry/Entity Type

Investment

Requirements
Should not have
• Graphs or people.

```html
<!DOCTYPE html>
<html lang="en">
<head>
<meta charset="utf-8">
<title>Tall Beacons – Value Investing</title>
<link href="https://fonts.googleapis.com/css2?family=Open+Sans:wght@400;600&family=Roboto:wght@300;400&family=PT+Sans&display=swap" rel="stylesheet">
<style>
:root{
  --bg:#000;
  --panel:#050505;
  --logo-bg:#1b1b1b;
  --orange:#f2a21b;
  --text:#a9a9a9;
  --text-light:#e6e6e6;
  --white:#fff;
  --rule:#2e2e2e;
  --box-border:#4a4a4a;
  --muted:#6f6f6f;
  --hero-blue:#1c1c52;
  --hero-magenta:#5a1240;
  --hero-violet:#3a1a66;
}
*{margin:0;padding:0;box-sizing:border-box}
html,body{width:823px;height:1200px;overflow:hidden;background:var(--bg)}
.page{width:1000px;height:1458px;position:relative;transform:scale(.823);transform-origin:0 0;font-family:"Open Sans",sans-serif;color:var(--text)}
a{color:var(--orange);text-decoration:none}
.abs{position:absolute}

.top-links{right:105px;top:34px;font-size:9px;color:var(--muted);letter-spacing:.2px}
.top-links a{color:#9a9a9a}
.top-links a.active{color:var(--orange)}
.top-links span{margin:0 6px}
.header-cta{right:105px;top:70px;font-family:"Roboto",sans-serif;font-weight:300;font-size:20px;color:var(--white);text-shadow:0 0 10px rgba(255,255,255,.7)}

.logo{left:117px;top:50px;width:213px;height:62px;background:var(--logo-bg);display:flex;align-items:center;padding-left:8px;gap:6px}
.logo-name{font-family:"PT Sans",sans-serif;font-size:33px;color:#e9e9e9}
.logo-dot{width:8px;height:8px;border-radius:50%;background:#e9e9e9;margin-top:10px}

.hero{left:15px;top:115px;width:928px;height:230px;
  background:linear-gradient(90deg,var(--hero-blue) 0%,#000 14%,#000 50%,var(--hero-magenta) 68%,var(--hero-violet) 84%,var(--hero-blue) 100%)}
.hero-title{left:123px;top:183px;width:380px;font-family:"Roboto",sans-serif;font-weight:300;font-size:20px;line-height:27px;color:#c9c9c9}
.hero-title em{font-style:normal;color:var(--orange)}

.side-nav{left:103px;top:388px;width:220px;list-style:none}
.side-nav li{font-size:9.5px;color:#ddd;height:20.7px;line-height:16px;border-bottom:1px dotted var(--rule);padding-left:10px;position:relative}
.side-nav li::before{content:"";position:absolute;left:1px;top:5px;width:5px;height:5px;border-radius:50%;background:var(--orange)}
.side-nav li.current{color:var(--orange)}

.promo{left:103px;width:222px;border:1px solid var(--box-border);text-align:center;overflow:hidden;
  background:linear-gradient(to top,rgba(90,40,130,.45),transparent 35%),var(--panel)}
.promo-trial{top:636px;height:162px}
.promo-trial h2{font-family:"Roboto",sans-serif;font-weight:300;font-size:26px;color:var(--orange);margin-top:12px}
.promo-trial p{font-family:"Roboto",sans-serif;font-size:13px;line-height:17.5px;color:var(--white);margin:10px 18px 0}
.promo-reg{top:820px;height:74px}
.promo-reg span{display:block;font-family:"Roboto",sans-serif;font-weight:300;font-size:23px;color:var(--white);margin-top:21px;text-shadow:0 0 8px rgba(255,255,255,.6)}

.main{left:387px;top:383px;width:490px}
.main h1,.main h2{font-family:"Roboto",sans-serif;font-weight:300;color:var(--orange);line-height:19px}
.main h1{font-size:18.5px}
.main h2{font-size:18.5px}
.main p{font-size:9.8px;line-height:15.5px;margin-bottom:15.5px;letter-spacing:.55px}
.main p.strong{color:var(--text-light);font-weight:600;letter-spacing:.4px}
.main p em{font-style:normal;color:var(--orange)}
.intro{margin-top:10px}
.divider{border-top:1px dotted var(--rule);margin:18px 0 16px}
.solved p:first-of-type{margin-top:18px}

.stats{left:120px;top:1035px;width:786px;display:grid;grid-template-columns:repeat(4,190px);column-gap:9px;row-gap:10px}
.stat{height:94px;border:1px solid var(--box-border);background:var(--panel);font-family:"Roboto",sans-serif;font-size:13px;line-height:18px;color:var(--white);text-align:center;padding-top:14px}
.stat b{font-weight:400;color:var(--orange)}

.rule{left:120px;width:786px;border-top:1px dotted var(--rule)}
.contact{left:121px;top:1270px;width:770px;font-size:7.8px;line-height:11.5px;color:#bbb;letter-spacing:.35px}
.legal{left:120px;top:1337px;width:790px;font-size:6.6px;line-height:9.6px;color:#6a6a6a;letter-spacing:.3px}
</style>
</head>
<body>
<div class="page">
  <nav class="top-links abs"><a class="active">Login</a><span>|</span><a>Register for free</a><span>|</span><a>Contact us</a><span>|</span><a>Terms &amp; Conditions</a></nav>
  <div class="header-cta abs">Free Registration</div>

  <div class="logo abs"><span class="logo-name">Tall Beacons</span><span class="logo-dot"></span></div>

  <div class="hero abs" role="img" aria-label="Abstract banner image of coloured light"></div>
  <p class="hero-title abs">A potential return of <em>23.57 %</em> a year from America’s biggest businesses with the emphasis firmly on capital preservation</p>

  <ul class="side-nav abs">
    <li class="current">Home</li>
    <li>Two Minute Guide</li>
    <li>Current &amp; year to date performance</li>
    <li>Watch list</li>
    <li>Other key numbers</li>
    <li>The back testing model and the results</li>
    <li>History of all trades</li>
    <li>FAQs</li>
    <li>About our analyses</li>
    <li>About value investing</li>
    <li>The Broadcap 1000 and the Meridian 500 index</li>
  </ul>

  <div class="promo promo-trial abs">
    <h2>Free trial period</h2>
    <p>if you would like to monitor our service free of charge for six months, then please complete <a>the registration form</a></p>
  </div>
  <div class="promo promo-reg abs"><span>Free Registration</span></div>

  <main class="main abs">
    <h1>A methodical and consistent software-driven process for identifying, and investing in, undervalued stocks</h1>
    <p class="intro">The attractions of value investing need no explanation to those who subscribe to the concept. But it’s impractical, if not impossible, for the private investor to implement the strategy (using direct holdings as distinct to collective funds) consistently. Although the data may be available, to undertake fundamental analysis regularly, on a reasonable number of stocks, entails a significant amount of time and effort.</p>
    <p>By definition - and depending on where you look and market conditions - undervalued businesses (stocks) are relatively scarce. So where does the value investor begin their search? Which and how many businesses must be scrutinised before one undervalued entity is found? And having identified a stock that’s trading at less than its fair value, will that be the case next week or next month? Fundamentals can change for the worse at any time, so without the benefit of regular analysis, how will the value investor know when to disinvest?</p>
    <div class="divider"></div>
    <section class="solved">
      <h2>Those problems - and others - have now been solved</h2>
      <p class="strong">Our software produces the quantitative analysis value investors need.</p>
      <p>Once a month, month in month out, our program scrutinises the key fundamentals of 1,000 large cap American companies which between them account for <em>92%</em> of the US securities market.</p>
      <p>First of all, the program sifts through each of the 1,000 stocks searching for favourable arrays of fundamentals: that process usually filters out between 950 and 975 stocks. The software then applies a range of algorithms to the short-listed stocks to identify any which are trading at <em>35%</em> (or more) below their estimated fair value. There are times when not one single stock on the shortlist meets our criteria. But when they do - and if there’s room - those stocks are added to our portfolio.</p>
      <p>We’re not stock pickers, share tippers or brokers. What we do is use software to analyse and identify stocks that appear to be undervalued.</p>
      <p class="strong">For more details and the results to date... <a>please go here</a></p>
      <p><a>More about the strategy we use to choose stocks...</a></p>
    </section>
  </main>

  <div class="rule abs" style="top:1010px"></div>

  <section class="stats abs">
    <div class="stat">Average, annualised<br>compound return over to<br><b>23.57 %</b></div>
    <div class="stat">So far this year,<br>the portfolio’s return is<br><b>13.49 %</b></div>
    <div class="stat">Worst ever annual loss:<br>-1.48 %; best ever<br>annual gain:<br><b>69.77 %</b></div>
    <div class="stat">Average return per trade<br>including losing trades:<br><b>24.44 %</b></div>
    <div class="stat">Maximum number of<br>winning/losing trades<br>in a row:<br><b>11/4</b></div>
    <div class="stat">Average number of days a<br>stock stays in the portfolio:<br><b>287</b></div>
    <div class="stat">An average of five trades<br>a year and never more<br>than five holdings at any<br>one time.</div>
    <div class="stat">86 trades in total, of which<br>65 were profitable<br>- a success rate of<br><b>75.58 %</b></div>
  </section>

  <div class="rule abs" style="top:1260px"></div>
  <p class="contact abs">If you have any questions, please e-mail <a>info@tallbeacons.co.uk</a>. Although we’re very willing to answer queries about the way we pick stocks, please do keep in mind that as we’re giving this service away free of charge initially, we’re not inclined to expend time and energy debating the relative merits of value investing or fundamental analyses. Other than that, fire away!</p>
  <div class="rule abs" style="top:1328px"></div>
  <p class="legal abs">This website is published by Tall Beacons Ltd. Registered in England No. 08193527. Registered office: 14 Orchard Vale Lane London N9 4QT. This website and its content is the copyright of Tall Beacons Ltd - © Tall Beacons Ltd 2011. All rights reserved. Any redistribution or reproduction of part or all of the contents in any form is prohibited other than the following: you may print or download to a local hard disk extracts for your personal and non-commercial use only you may copy the content to individual third parties for their personal use, but only if you acknowledge the website as the source of the material. You may not, except with our express written permission, distribute or commercially exploit the content. Nor may you transmit it or store it in any other website or other form of electronic retrieval system.</p>
</div>
</body>
</html>
```